Podcast Cover Art Design for Divorce Support

Need a podcast cover art design for new podcast that will cover Emotional Divorce Support and Recovery topics. People are lost, confused. They are looking for help during the confusion and heartbreak. Main Title is "Quiet Harbor Podcast". Subtitle is "Finding Your Feet Again". We want a design that is encouraging yet not overly "happy". We also want to convey kindness, clarity, and strength, if possible. Our logo colors use grey and red though we aren't tied to those colors for the podcast. Logo may be used on the podcast but not required. Final image should be 3000x3000px. Our logo uses Montserrat-Medium and Multi-SemiBold. Not necessary but available if you want to use it.

```html
<!DOCTYPE html>
<html lang="en">
<head>
<meta charset="utf-8">
<title>Quiet Harbor Podcast – Cover Art</title>
<link href="https://fonts.googleapis.com/css2?family=Montserrat:wght@400;500;800&family=Roboto+Condensed:wght@400&display=swap" rel="stylesheet">
<style>
  :root {
    --stage: #e6e6e6;
    --panel-light: #f4f4f4;
    --panel-mid: #d3d4d6;
    --grey-box: #a7a9ac;
    --grey-rule: #b9babc;
    --ink: #0a0a0a;
    --red: #ec2227;
    --white: #ffffff;
  }
  * { margin: 0; padding: 0; box-sizing: border-box; }
  html, body {
    width: 1200px; height: 596px; overflow: hidden;
    background: var(--stage);
  }
  .cover {
    position: absolute; left: 302px; top: 0;
    width: 596px; height: 596px; overflow: hidden;
    background: var(--panel-mid);
  }
  .cover__texture {
    position: absolute; left: 23px; top: 23px; width: 555px; height: 466px;
    background: linear-gradient(135deg, var(--panel-light) 0%, #e2e3e4 45%, var(--panel-mid) 100%);
  }
  .cover__edge-red { position: absolute; left: 578px; top: 0; width: 18px; height: 466px; background: var(--red); }
  .cover__edge-grey { position: absolute; left: 14px; top: 23px; width: 9px; height: 299px; background: var(--grey-rule); }
  .title {
    position: absolute; left: 49px; line-height: 1; white-space: nowrap;
    font-family: "Montserrat", sans-serif;
  }
  .title--first { top: 36px; font-size: 113px; font-weight: 400; color: var(--ink); letter-spacing: 2px; }
  .title--accent { top: 140px; font-size: 103px; font-weight: 400; color: var(--red); }
  .title--format { top: 259px; font-size: 67px; font-weight: 800; color: var(--ink); }
  .subtitle-box { position: absolute; left: 0; top: 347px; width: 331px; height: 142px; background: var(--grey-box); }
  .subtitle-lead {
    position: absolute; left: 49px; top: 363px; line-height: 1; white-space: nowrap;
    font-family: "Roboto Condensed", sans-serif; font-size: 40px; color: var(--white);
  }
  .subtitle-key {
    position: absolute; left: 49px; top: 408px; line-height: 1; white-space: nowrap;
    font-family: "Montserrat", sans-serif; font-size: 67px; font-weight: 800; color: var(--ink);
  }
  .tag-band { position: absolute; left: 198px; top: 489px; width: 398px; height: 107px; background: var(--red); }
  .tag-text {
    position: absolute; right: 46px; top: 521px; line-height: 1; white-space: nowrap;
    font-family: "Roboto Condensed", sans-serif; font-size: 46px; color: var(--white);
  }
  .foot-red { position: absolute; left: 0; top: 575px; width: 175px; height: 21px; background: var(--red); }
  .foot-grey { position: absolute; left: 175px; top: 575px; width: 23px; height: 21px; background: var(--grey-box); }
  .brand {
    position: absolute; left: 378px; top: 380px; display: flex; align-items: center; gap: 8px;
  }
  .brand__dot { width: 18px; height: 18px; border-radius: 50%; background: var(--red); }
  .brand__name {
    font-family: "Montserrat", sans-serif; font-weight: 500; font-size: 24px; color: var(--grey-box);
  }
</style>
</head>
<body>
  <main class="cover">
    <div class="cover__texture" role="img" aria-label="Soft grey and white triangle and dot pattern background"></div>
    <div class="cover__edge-red"></div>
    <div class="cover__edge-grey"></div>

    <h1>
      <span class="title title--first">QUIET</span>
      <span class="title title--accent">HARBOR</span>
      <span class="title title--format">PODCAST</span>
    </h1>

    <div class="subtitle-box"></div>
    <p class="subtitle-lead">FINDING YOUR</p>
    <p class="subtitle-key">FEET</p>

    <div class="brand">
      <span class="brand__dot"></span>
      <span class="brand__name">Harborlight</span>
    </div>

    <div class="tag-band"></div>
    <p class="tag-text">AGAIN</p>

    <div class="foot-red"></div>
    <div class="foot-grey"></div>
  </main>
</body>
</html>
```